Velmora - New coded website

Current website is around 5 years old and corrupted in some ways...
I would like to refresh the design and to create a new coded website based on the current content .
Please refer to :
www.velmora-sample.com.au

Coded - Design and coding required

```html
<!DOCTYPE html>
<html lang="en">
<head>
<meta charset="utf-8">
<title>Velmora – Odours Controlled Naturally</title>
<link href="https://fonts.googleapis.com/css2?family=Playfair+Display:wght@400;600&family=Inter:wght@400;500;600&display=swap" rel="stylesheet">
<style>
:root{
  --green:#6cb33f;
  --green-dark:#4f9a2c;
  --navy:#0f4c75;
  --navy-deep:#0c2b42;
  --teal:#1d5f73;
  --ink:#222;
  --muted:#555;
  --sky:#e7f0f5;
  --grey-ring:#e6e9ec;
  --white:#fff;
}
*{box-sizing:border-box;margin:0;padding:0}
html,body{width:1200px;height:4470px;overflow:hidden;background:var(--white)}
body{font-family:"Inter",sans-serif;color:var(--ink);position:relative}
.serif{font-family:"Playfair Display",serif;font-weight:400}
.abs{position:absolute}
.btn{display:inline-flex;align-items:center;justify-content:center;gap:6px;background:var(--green);color:#fff;border-radius:20px;font-size:11px;font-weight:500}

/* hero */
.hero{position:absolute;left:0;top:0;width:1200px;height:620px;background:linear-gradient(180deg,#6d93c8 0%,#a9c4e0 18%,#3f6b2a 30%,#557e2c 45%,#7aa83a 70%,#5e9a2e 100%)}
.nav{position:absolute;left:187px;top:48px;width:826px;height:52px;background:#fff;border-radius:26px;display:flex;align-items:center;font-size:9.5px;color:#333}
.nav .left{position:absolute;left:38px;display:flex;gap:22px}
.nav .right{position:absolute;left:491px;display:flex;gap:20px}
.nav .contact{position:absolute;right:0;top:0;height:52px;width:120px;background:var(--green);color:#fff;border-radius:0 26px 26px 0;display:flex;align-items:center;justify-content:center;font-size:12px}
.brand-badge{position:absolute;left:548px;top:22px;width:104px;height:104px;border-radius:50%;background:#fff;display:flex;align-items:center;justify-content:center;font-family:"Playfair Display",serif;font-size:17px;color:var(--navy)}
.hero-box{position:absolute;left:355px;top:222px;width:491px;height:258px;background:var(--navy);text-align:center;color:#fff}
.hero-box .eyebrow{margin-top:34px;color:var(--green);font-size:14px;letter-spacing:2px}
.hero-box h1{font-family:"Playfair Display",serif;font-weight:400;font-size:52px;line-height:54px;margin-top:6px}
.hero-box .rule{position:absolute;top:136px;width:102px;height:2px;background:var(--green)}
.hero-box .btn{margin-top:20px;width:164px;height:34px}

/* features */
.feature{position:absolute;width:260px;text-align:center}
.feature .label{font-family:"Playfair Display",serif;font-size:28px;color:#222}

/* about */
.about-photo{position:absolute;left:0;top:1193px;width:1200px;height:546px;background:linear-gradient(90deg,#a88a4f 0%,#c7a767 35%,#8fa3b5 70%,#6a7c56 100%)}
.about-card{position:absolute;left:186px;top:1290px;width:345px;height:449px;background:#fff;text-align:center;padding:80px 30px 0}
.about-card h2{font-family:"Playfair Display",serif;font-weight:400;font-size:34px}
.about-card p{font-size:12.5px;line-height:19.5px;color:#444;margin-top:10px}
.about-card .btn{margin-top:22px;width:164px;height:36px}

/* video */
.video-band{position:absolute;left:0;top:1739px;width:1200px;height:377px;background:linear-gradient(180deg,#6cb33f 0%,#3b8b4e 45%,#0f4c75 100%)}
.video-card{position:absolute;left:187px;top:1904px;width:826px;height:381px;border-radius:26px;overflow:hidden;background:#fbfdf7;box-shadow:0 10px 30px rgba(0,0,0,.15)}

/* best */
.best h2{font-family:"Playfair Display",serif;font-weight:400;font-size:36px;line-height:38px}
.ticks{list-style:none;font-size:12.5px;color:#333}
.ticks li{display:flex;align-items:center;gap:8px;height:30px}

/* testimonials */
.testi{position:absolute;top:2986px;height:335px;border-radius:6px;background:#fff;padding:36px 36px 0;font-size:12.5px;line-height:27.5px;color:#555;box-shadow:0 6px 20px rgba(0,0,0,.06);overflow:hidden}
.testi .quote{height:220px;overflow:hidden}
.testi.active{background:var(--green);color:#fff}
.testi .who{position:absolute;left:36px;bottom:18px;display:flex;align-items:center;gap:12px;line-height:16px}
.testi .who b{font-family:"Playfair Display",serif;font-size:14px;display:block}
.testi .who small{font-size:9.5px}
.testi .stars{position:absolute;right:36px;bottom:26px;color:#f5b52e;letter-spacing:8px;font-size:15px;line-height:15px}
.testi .divider{position:absolute;left:36px;right:36px;bottom:70px;height:1px;background:rgba(0,0,0,.12)}
.testi.active .divider{background:rgba(255,255,255,.35)}
.avatar{width:34px;height:34px;border-radius:50%;background:#c9b9c9;border:2px solid #fff}

/* contact */
.touch-item{position:absolute;top:3583px;display:flex;gap:16px;align-items:flex-start}
.touch-item .ic{width:68px;height:68px;border-radius:50%;background:var(--green);display:flex;align-items:center;justify-content:center}
.touch-item h4{font-family:"Playfair Display",serif;font-weight:400;font-size:16px;margin-top:12px}
.touch-item p{font-size:11px;color:#777;line-height:15px;margin-top:4px}
.form-card{position:absolute;left:187px;top:3693px;width:826px;height:301px;background:#fff;border-radius:6px;box-shadow:0 8px 24px rgba(0,0,0,.1);text-align:center}
.field{position:absolute;background:#f1f3f5;border-radius:3px;font-size:11px;color:#777;padding:12px 16px;text-align:left}

/* footer */
.footer{position:absolute;left:0;top:3829px;width:1200px;height:641px;background:var(--navy-deep);color:#fff}
.newsletter-input{position:absolute;left:607px;top:4066px;width:288px;height:40px;background:#133b55;border-radius:20px 0 0 20px;font-size:11px;color:#9fb3c2;display:flex;align-items:center;padding-left:40px}
.newsletter-btn{position:absolute;left:895px;top:4066px;width:118px;height:40px;background:var(--green);border-radius:0 20px 20px 0;font-size:12px;display:flex;align-items:center;justify-content:center}
.links{list-style:none;font-size:11px;color:#b9c7d2;line-height:23px}
.links li::before{content:"•";margin-right:8px}
.bottom-bar{position:absolute;left:187px;top:4418px;width:826px;height:1px;background:rgba(255,255,255,.15)}
.legal{position:absolute;top:4437px;font-size:10.5px;color:#b9c7d2}
</style>
</head>
<body>

<!-- HERO -->
<section class="hero" role="img" aria-label="Photograph of a sunny park with green lawn and trees"></section>
<svg class="abs" style="left:0;top:500px" width="1200" height="140" viewBox="0 0 1200 140">
  <path d="M0 70 Q420 140 1200 38 L1200 140 L0 140Z" fill="#fff"/>
  <path d="M0 70 Q420 140 1200 38" fill="none" stroke="#6cb33f" stroke-width="9"/>
</svg>
<nav class="nav">
  <div class="left"><span>Odour Control Products</span><span>How Biofiltration Works</span><span>About Us</span></div>
  <div class="right"><span>Odour Control by Industry</span><span>Past Projects</span></div>
  <div class="contact">Contact Us</div>
</nav>
<div class="brand-badge">Velmora</div>
<div class="hero-box">
  <p class="eyebrow">Wellcome To Velmora</p>
  <h1>Odours Controlled<br>Naturally</h1>
  <span class="rule" style="left:24px"></span><span class="rule" style="right:24px"></span>
  <a class="btn">Request a Quote →</a>
</div>

<!-- FEATURES -->
<svg class="abs" style="left:0;top:690px" width="1200" height="420" viewBox="0 690 1200 420">
  <defs>
    <linearGradient id="arcGrad" x1="0" y1="0" x2="1" y2="0"><stop offset="0" stop-color="#0f4c75"/><stop offset="1" stop-color="#6cb33f"/></linearGradient>
  </defs>
  <path d="M196 845 A130 130 0 0 1 452 830" fill="none" stroke="url(#arcGrad)" stroke-width="11"/>
  <circle cx="204" cy="848" r="13" fill="#0f4c75"/><circle cx="204" cy="848" r="5" fill="#fff"/>
  <circle cx="326" cy="845" r="98" fill="#fff" stroke="#e6e9ec" stroke-width="10"/>
  <g fill="none" stroke="#6cb33f" stroke-width="3"><rect x="306" y="806" width="60" height="40"/><path d="M300 856 h30 l20 10 h20"/><path d="M290 846 v28"/></g>
  <path d="M754 845 A130 130 0 0 1 1010 830" fill="none" stroke="url(#arcGrad)" stroke-width="11"/>
  <circle cx="762" cy="848" r="13" fill="#0f4c75"/><circle cx="762" cy="848" r="5" fill="#fff"/>
  <circle cx="884" cy="845" r="98" fill="#fff" stroke="#e6e9ec" stroke-width="10"/>
  <g fill="none" stroke="#6cb33f" stroke-width="3"><circle cx="884" cy="845" r="38"/><path d="M884 822 v23 l16 10"/></g>
  <path d="M476 936 A130 130 0 0 0 732 950" fill="none" stroke="url(#arcGrad)" stroke-width="11"/>
  <circle cx="484" cy="927" r="13" fill="#0f4c75"/><circle cx="484" cy="927" r="5" fill="#fff"/>
  <circle cx="600" cy="936" r="98" fill="#fff" stroke="#e6e9ec" stroke-width="10"/>
  <g fill="none" stroke="#6cb33f" stroke-width="3"><path d="M580 906 l4 8 9 1-7 6 2 9-8-5-8 5 2-9-7-6 9-1z"/><path d="M580 935 l4 8 9 1-7 6 2 9-8-5-8 5 2-9-7-6 9-1z"/><path d="M602 902h40M602 914h40M602 932h40M602 944h40M602 962h40"/></g>
</svg>
<div class="feature" style="left:196px;top:950px"><span class="label">Products</span></div>
<div class="feature" style="left:754px;top:950px"><span class="label">Past Projects</span></div>
<div class="feature" style="left:470px;top:1075px"><span class="label">Features</span></div>

<!-- ABOUT -->
<section class="about-photo" role="img" aria-label="Photograph of a woman with arms outstretched in a golden grass field"></section>
<div class="about-card">
  <h2>About Odours</h2>
  <p>Velmora uses sustainable biotechnology to resolve odour and <u>corrosion</u> problems in a highly efficient, environmentally friendly and cost-effective manner.</p>
  <p style="margin-top:18px">Our products, the VelVent series of biofilters have been specifically engineered to overcome issues traditionally associated with biofiltration, such as bed compaction and uneven moisture levels, and our patented design achieves a removal rate of up to 99.9% per stage of treatment.</p>
  <a class="btn">Read More →</a>
</div>
<div class="abs" style="left:310px;top:1252px;width:96px;height:96px;border-radius:50%;background:#fff;box-shadow:0 2px 8px rgba(0,0,0,.1)"></div>

<!-- VIDEO -->
<section class="video-band"></section>
<h2 class="abs serif" style="left:0;top:1822px;width:1200px;text-align:center;font-size:34px;color:#fff">Watch Our Video</h2>
<div class="video-card">
  <div class="abs" role="img" aria-label="Illustration of trees, biofilter tanks and eco icons" style="left:30px;top:50px;width:766px;height:331px;background:linear-gradient(180deg,#fbfdf7 0%,#e8f4d8 45%,#8fcf6a 75%,#1a9b8a 100%)"></div>
  <svg class="abs" style="left:366px;top:128px" width="94" height="94" viewBox="0 0 94 94"><circle cx="47" cy="47" r="47" fill="#0f2a3a"/><path d="M40 35 L60 47 L40 59Z" fill="#fff"/></svg>
</div>

<!-- WHAT MAKES US BEST -->
<section class="best">
  <h2 class="abs" style="left:187px;top:2406px">What makes us<br>the best?</h2>
  <p class="abs" style="left:187px;top:2500px;width:370px;font-size:12px;line-height:19.5px;color:#444">It was popularised in the 1960s with the release of Letterline sheets containing Lorem Ipsum passages, and more recently with desktop publishing software like Pagecraft Studio.</p>
  <ul class="ticks abs" style="left:187px;top:2577px">
    <li><svg width="16" height="16" viewBox="0 0 16 16"><circle cx="8" cy="8" r="7" fill="none" stroke="#6cb33f" stroke-width="1.5"/><path d="M4.5 8.2l2.3 2.3 4.7-4.8" fill="none" stroke="#6cb33f" stroke-width="1.6"/></svg>Biological &amp; Sustainable technology</li>
    <li><svg width="16" height="16" viewBox="0 0 16 16"><circle cx="8" cy="8" r="7" fill="none" stroke="#6cb33f" stroke-width="1.5"/><path d="M4.5 8.2l2.3 2.3 4.7-4.8" fill="none" stroke="#6cb33f" stroke-width="1.6"/></svg>Efficient maintenance cost</li>
    <li><svg width="16" height="16" viewBox="0 0 16 16"><circle cx="8" cy="8" r="7" fill="none" stroke="#6cb33f" stroke-width="1.5"/><path d="M4.5 8.2l2.3 2.3 4.7-4.8" fill="none" stroke="#6cb33f" stroke-width="1.6"/></svg>100% Australian Owned</li>
    <li><svg width="16" height="16" viewBox="0 0 16 16"><circle cx="8" cy="8" r="7" fill="none" stroke="#6cb33f" stroke-width="1.5"/><path d="M4.5 8.2l2.3 2.3 4.7-4.8" fill="none" stroke="#6cb33f" stroke-width="1.6"/></svg>Eco Friendly</li>
  </ul>
  <svg class="abs" style="left:595px;top:2350px" width="420" height="400" viewBox="0 0 420 400">
    <path d="M220 8 A194 194 0 0 1 330 355" fill="none" stroke="#6cb33f" stroke-width="8"/>
  </svg>
  <div class="abs" role="img" aria-label="Portrait photograph of a woman breathing fresh air" style="left:607px;top:2355px;width:388px;height:388px;border-radius:50%;background:radial-gradient(circle at 50% 40%,#c9a58a 0%,#7a5a40 45%,#3e4a2e 100%)"></div>
  <div class="abs" style="left:589px;top:2613px;width:132px;height:132px;border-radius:50%;background:#fff;border:6px solid #6cb33f"></div>
</section>

<!-- TESTIMONIALS -->
<svg class="abs" style="left:0;top:2700px" width="1200" height="730" viewBox="0 0 1200 730">
  <path d="M0 50 Q560 230 1200 22 L1200 725 L0 725Z" fill="#e7f0f5"/>
  <path d="M0 50 Q560 230 1200 22" fill="none" stroke="#6cb33f" stroke-width="9"/>
</svg>
<h2 class="abs serif" style="left:0;top:2900px;width:1200px;text-align:center;font-size:34px">Our Testimonials</h2>
<div class="testi" style="left:-368px;width:628px">
  <p class="quote">"Rhys and the Velmora team promised to stop the odour from our smelly neighbor<br>and they delivered- in spades! As soon as the system was started, the smell<br>disappeared. The system is well designed, very professionally installed and the<br>beauty of it is, apart from a constantly running fan, it is bacteria doing the heavy<br>lifting, so it is very environmentally friendly. We lived with the smell for 3 three<br>years which could be extremely frustrating and unpleasant. Now, the problem is<br>solved and we can have BBQs again. We are happy and our neighbours have</p>
  <span class="divider"></span><span class="stars">★★★★★</span>
</div>
<div class="testi active" style="left:286px;width:628px">
  <p class="quote" style="height:230px">"Rhys and the Velmora team promised to stop the odour from our smelly neighbor<br>and they delivered- in spades! As soon as the system was started, the smell<br>disappeared. The system is well designed, very professionally installed and the<br>beauty of it is, apart from a constantly running fan, it is bacteria doing the heavy<br>lifting, so it is very environmentally friendly. We lived with the smell for 3 three<br>years which could be extremely frustrating and unpleasant. Now, the problem is<br>solved and we can have BBQs again. We are happy and our neighbours have<br>noticed the odour is gone. Thank you!"</p>
  <span class="divider"></span>
  <div class="who"><span class="avatar"></span><span><b>Liam.</b><small>Designation Here</small></span></div>
  <span class="stars">★★★★★</span>
</div>
<div class="testi" style="left:940px;width:628px;white-space:nowrap">
  <p class="quote" style="height:230px">"Rhys and the Velmora team promised to stop the odour from our smelly neighbor<br>and they delivered- in spades! As soon as the system was started, the smell<br>disappeared. The system is well designed, very professionally installed and the<br>beauty of it is, apart from a constantly running fan, it is bacteria doing the heavy<br>lifting, so it is very environmentally friendly. We lived with the smell for 3 three<br>years which could be extremely frustrating and unpleasant. Now, the problem is<br>solved and we can have BBQs again. We are happy and our neighbours have<br>noticed the odour is gone. Thank you!"</p>
  <span class="divider"></span>
  <div class="who"><span class="avatar"></span><span><b>Owen</b><small>Designation Here</small></span></div>
</div>

<!-- GET IN TOUCH -->
<h2 class="abs serif" style="left:0;top:3506px;width:1200px;text-align:center;font-size:34px">Get In Touch</h2>
<div class="touch-item" style="left:252px">
  <span class="ic"><svg width="26" height="26" viewBox="0 0 26 26" fill="none" stroke="#fff" stroke-width="2.2"><circle cx="13" cy="13" r="8"/><circle cx="13" cy="13" r="2.5" fill="#fff"/><path d="M13 1v5M13 20v5M1 13h5M20 13h5"/></svg></span>
  <div><h4>Address</h4><p>12 Sample Grove, Northvale<br>WA 6000, Australia</p></div>
</div>
<div class="touch-item" style="left:519px">
  <span class="ic"><svg width="24" height="24" viewBox="0 0 24 24"><path d="M6 2l4 5-2.5 2.5a13 13 0 0 0 7 7L17 14l5 4-2.5 3.5C11 21 3 13 2.5 4.5Z" fill="#fff"/></svg></span>
  <div><h4>Phone</h4><p>+61 (08) 5550 0123</p></div>
</div>
<div class="touch-item" style="left:760px">
  <span class="ic"><svg width="26" height="20" viewBox="0 0 26 20"><rect x="1" y="1" width="24" height="18" rx="2" fill="#fff"/><path d="M2 3l11 8 11-8" fill="none" stroke="#6cb33f" stroke-width="2"/></svg></span>
  <div><h4>Email</h4><p>info@velmora-sample.com.au</p></div>
</div>

<!-- FOOTER (navy base) -->
<footer class="footer"></footer>

<!-- CONTACT FORM -->
<div class="form-card">
  <h2 class="serif" style="font-size:34px;margin-top:26px">Contact Us</h2>
  <div class="field" style="left:92px;top:84px;width:205px;height:40px">Name</div>
  <div class="field" style="left:310px;top:84px;width:205px;height:40px">Email</div>
  <div class="field" style="left:531px;top:84px;width:205px;height:40px">Phone</div>
  <div class="field" style="left:92px;top:139px;width:644px;height:73px">Message</div>
  <a class="btn abs" style="left:338px;top:233px;width:164px;height:36px">Submit Now →</a>
</div>

<!-- NEWSLETTER & FOOTER CONTENT -->
<h2 class="abs serif" style="left:187px;top:4056px;font-size:30px;line-height:36px;color:#fff">Sign Up For Our<br>Newsletter</h2>
<div class="newsletter-input"><svg class="abs" style="left:20px;top:15px" width="12" height="10" viewBox="0 0 12 10"><rect width="12" height="10" rx="1" fill="#9fb3c2"/></svg>Enter Email Address</div>
<div class="newsletter-btn" style="color:#fff">Submit Now →</div>

<div class="abs" style="left:187px;top:4192px;display:flex;align-items:center;gap:10px">
  <span style="width:46px;height:46px;border-radius:50%;background:var(--green);display:block"></span>
  <span class="serif" style="font-size:28px;color:#fff">Velmora</span>
</div>
<h4 class="abs serif" style="left:417px;top:4206px;font-size:15px;color:#fff">Quick Links</h4>
<ul class="links abs" style="left:417px;top:4238px">
  <li>Odour Control Products</li>
  <li>How Biofiltration Works</li>
  <li>Odour Control by Industry</li>
  <li>Past Projects</li>
  <li>About Us</li>
</ul>
<div class="abs" role="img" aria-label="Street map showing the office location" style="left:610px;top:4189px;width:403px;height:172px;background:linear-gradient(135deg,#f2f3f1 0%,#e7ecef 60%,#dfe9dc 100%);border:6px solid #fff;border-radius:4px"></div>

<div class="bottom-bar"></div>
<p class="legal" style="left:187px">© 2023 velmora-sample.com.au All Rights Reserved</p>
<p class="legal" style="left:735px">Privacy Policy &nbsp;&nbsp;|&nbsp;&nbsp; Sitemap &nbsp;&nbsp;|&nbsp;&nbsp; ABN: 00 000 000 000</p>

</body>
</html>
```